Personal Trainer website design

We are working with a personal trainer to design a website. They offer their primary services: Diet Coaching, In-Person Coaching (workouts), and Remote Coaching.
Some sites we like: https://www.marenkoltby.com, https://tavilobrenn.com/en-us, https://corevandel.co.uk
Thank you for taking the time to consider designing a website for us. We are web developers based in Stockton, CA USA. Most of our projects go through the same process. Understanding this process may help you win a project with us. We custom-code all of our websites in-house. We don’t have any requirements as to what tools you use for your design, but ask that you follow these guidelines.
IMAGES:
We ask that if you use any images, or icons in the design, have a link to the asset, so we can purchase the image/icon. Most of the designs we submit do not have the customer’s images on them unless they have some great images. Be creative; show us the feeling that you are trying to portray with your image choices. Use any royalty-free site you choose. We subscribe to Quillex and mostly use their images, but are ok to purchase images outside of Quillex.
FONTS:
We ask that you identify the fonts you’re using in the design. This can be done in a message if you want. We typically use Brimora Fonts and Quillex Fonts.
CONTENT:
We're always open to different content and ideas. Often, we submit designs with stock images so that the client can see our vision. We typically go back and take pictures after the website launch to use their images with our vision. Lorem Ipsum is fine for paragraphs, but we ask that you make the Headers with correct English. We want to be able to show the vision and identify the sections of the website.
INSPIRATION:
We try and add a couple of links in the brief of some websites that we like to help you get started in your design.
REVISIONS:
We do not often ask for revisions of the designs unless we see something in the design that may not appeal to the client. If there are slight changes that we want to make, we simply do that in the development process.
FEEDBACK:
We rarely give feedback on designs during the design process. We are working on many website projects and do not have the time to give feedback. We usually respond if your request is well thought out and asks specific questions, but a note asking “feedback, please” usually goes unanswered.
1 page

```html
<!DOCTYPE html>
<html lang="en">
<head>
<meta charset="utf-8">
<title>Veltrafit – Personal Trainer</title>
<link rel="stylesheet" href="https://fonts.googleapis.com/css2?family=Bebas+Neue&family=DM+Serif+Display&family=Inter:wght@400;500;600&display=swap">
<style>
:root{
  --backdrop:#e8ebd3;
  --backdrop-mark:#c6cab2;
  --green:#8a9a1b;
  --ink:#222;
  --muted:#555;
  --card:#efefef;
  --footer:#d9d5cf;
  --white:#fff;
  --serif:'DM Serif Display', Georgia, serif;
  --sans:'Inter', Arial, sans-serif;
  --display:'Bebas Neue', Impact, sans-serif;
}
*{margin:0;padding:0;box-sizing:border-box}
html,body{width:1200px;height:1200px;overflow:hidden;background:var(--backdrop)}
.stage{position:absolute;left:0;top:0;width:1932px;height:1932px;transform:scale(.62112);transform-origin:0 0;background:var(--backdrop);font-family:var(--sans);color:var(--ink)}
.backdrop-mark{position:absolute;left:305px;top:1455px;transform:rotate(-90deg);transform-origin:0 0;font-family:var(--display);font-size:275px;line-height:.75;letter-spacing:22px;color:var(--backdrop-mark);white-space:nowrap}
.backdrop-dot{position:absolute;left:270px;top:770px;width:285px;height:285px;border-radius:50%;background:#dfe1bf}
.page{position:absolute;left:680px;top:111px;width:572px;height:1709px;background:var(--white);overflow:hidden;box-shadow:0 4px 20px rgba(0,0,0,.08)}
.abs{position:absolute}
.photo{position:absolute;border-radius:4px}
.pill{position:absolute;border-radius:20px;background:var(--green);color:var(--white);font-size:4.5px;font-weight:500;display:flex;align-items:center;justify-content:center;letter-spacing:.2px}
.pill.grey{background:#ddd;color:#444}
.label{font-size:6px;color:var(--ink)}
.title{font-family:var(--serif);font-size:12.5px;color:var(--ink)}
.title em{font-style:normal;color:var(--green)}
.body{font-size:4.4px;line-height:7.2px;color:#333}
/* hero */
.hero{left:0;top:0;width:572px;height:269px;background:linear-gradient(120deg,#b9b9b7 0%,#cfcfcd 45%,#a4a3a0 75%,#8a8580 100%)}
.hero-shade{position:absolute;inset:0;background:rgba(40,40,40,.18)}
.brand-box{left:62px;top:0;width:144px;height:69px;background:rgba(235,235,235,.75);border-radius:0 0 10px 10px;display:flex;align-items:center;justify-content:center;gap:5px}
.brand-name{font-family:var(--display);font-size:34px;color:#2b2b2b;letter-spacing:1px}
.brand-dot{width:14px;height:14px;border-radius:50%;background:var(--green)}
.social{display:flex;gap:4px}
.social span{width:10px;height:10px;border-radius:50%;background:var(--green)}
.hero-social{left:424px;top:17px}
.nav{right:60px;top:35px;display:flex;align-items:center;gap:7px;font-size:4.5px;color:var(--white);letter-spacing:.2px}
.nav .members{position:static;width:38px;height:13px}
.search-dot{width:10px;height:10px;border-radius:50%;background:var(--green)}
.hero-copy{left:136px;width:300px;top:100px;text-align:center;color:var(--white)}
.hero-copy .kicker{font-size:6px}
.hero-copy h1{font-family:var(--serif);font-weight:400;font-size:19px;line-height:19px;margin-top:5px}
.hero-copy .author{font-size:6px;margin-top:2px;padding-left:90px}
.hero-copy p{font-size:4.4px;line-height:7px;margin:8px 26px 0}
/* frames */
.frame{position:absolute;border:1.5px solid var(--green);border-right:none;border-bottom:none;border-radius:4px 0 0 0}
.frame.br{border:1.5px solid var(--green);border-left:none;border-top:none;border-radius:0 0 4px 0}
/* list */
.checks{list-style:none}
.checks li{display:flex;align-items:center;gap:4px;font-size:4.4px;height:10px}
.checks svg{width:6px;height:6px}
/* services */
.services-title{font-family:var(--display);font-size:13px;letter-spacing:.3px}
.services-title em{font-style:normal;color:var(--green)}
.svc{position:absolute;width:134px;height:134px;border-radius:4px;overflow:hidden;color:var(--white)}
.svc .veil{position:absolute;inset:0;background:rgba(0,0,0,.22)}
.svc h3{position:absolute;left:9px;top:34px;font-family:var(--serif);font-weight:400;font-size:9.5px}
.svc .rule{position:absolute;left:9px;top:49px;width:14px;height:1px;background:var(--white)}
.svc p{position:absolute;left:9px;top:56px;width:118px;font-size:4.3px;line-height:7px}
.svc .more{position:absolute;left:9px;top:85px;width:42px;height:9px;background:var(--white);color:#333;border-radius:10px;font-size:4.3px;display:flex;align-items:center;justify-content:center;gap:3px}
/* featured */
.press{left:75px;top:1122px;width:420px;height:67px;background:#efefef;border-radius:4px;display:grid;grid-template-columns:repeat(5,1fr);align-items:center;justify-items:center;padding:6px 8px}
.press span{font-family:var(--serif);font-size:12px;color:#555;white-space:nowrap}
/* testimonials */
.t-heading{font-family:var(--serif);font-size:10.5px;line-height:11.5px}
.stars{color:var(--green);font-size:7px;letter-spacing:1.5px}
.rating{font-family:var(--serif);font-size:9.5px}
.t-card{position:absolute;top:1218px;width:135px;height:158px;background:var(--card);border-radius:4px;text-align:center}
.t-card .avatar{margin:16px auto 0;width:56px;height:56px;border-radius:50%;border:1px solid #bbb}
.t-card .name{color:var(--green);font-size:6.5px;margin-top:12px}
.t-card .role{font-size:4px;color:#555;margin-top:1px}
.t-card .stars{font-size:5px;margin-top:3px}
.t-card p{font-size:4.3px;line-height:6.8px;color:#666;margin:4px 8px 0}
/* subscribe */
.sub-title{font-family:var(--serif);font-size:11px}
.sub-title em{font-style:normal;color:var(--green)}
.email{left:325px;top:1473px;width:170px;height:21px;border-radius:11px;background:#eee;font-size:4.4px;color:#555;display:flex;align-items:center;padding-left:10px}
.email .pill{right:0;top:0;width:55px;height:21px;font-size:5px}
/* footer */
.footer{left:0;top:1586px;width:572px;height:123px;background:var(--footer)}
.f-brand{left:75px;top:35px;display:flex;align-items:center;gap:4px}
.f-brand .brand-name{font-size:27px}
.f-brand .brand-dot{width:11px;height:11px}
.f-head{font-size:8px;letter-spacing:.3px}
.f-small{font-size:5px;color:#333}
.f-links{font-size:5.4px;line-height:10.5px;color:#333}
.cards{display:flex;gap:3px}
.cards span{width:13px;height:8px;border-radius:1.5px;background:#fff;border:.6px solid #aaa}
</style>
</head>
<body>
<div class="stage">
  <div class="backdrop-dot"></div>
  <div class="backdrop-mark">VELTRAFIT</div>

  <main class="page">
    <!-- Hero -->
    <section class="abs hero" role="img" aria-label="Photo of a trainer stretching a client on a mat in a bright studio">
      <div class="hero-shade"></div>
    </section>
    <div class="abs brand-box"><span class="brand-name">VELTRAFIT</span><span class="brand-dot"></span></div>
    <div class="abs social hero-social"><span></span><span></span><span></span><span></span><span></span></div>
    <nav class="abs nav">
      <span>ABOUT</span><span>SERVICES</span><span>THE JOURNAL</span><span>BLOG</span><span>SHOP</span><span>CONTACT</span>
      <span class="pill members">MEMBERS</span><span class="search-dot"></span>
    </nav>
    <div class="abs hero-copy">
      <div class="kicker">Your personal workout and diet trainer</div>
      <h1>A healthy outside starts from<br>the inside.</h1>
      <div class="author">– Dorian Vales</div>
      <p>Lorem ipsum dolor sit amet, consectetur adipiscing elit. Vestibulum vel fringilla mi. Integer eu sagittis quam, sit amet volutpat odio. Sed et tincidunt nisi. Integer eget felis quis nulla tincidunt commodo. Sed at tincidunt eros.</p>
    </div>
    <div class="pill" style="left:263px;top:209px;width:45px;height:14px">GET STARTED</div>

    <!-- About -->
    <div class="abs label" style="left:75px;top:335px">Our Mission, Vission, Passion and History</div>
    <div class="abs title" style="left:75px;top:350px">About <em>Veltrafit</em></div>
    <p class="abs body" style="left:75px;top:370px;width:172px">Curabitur tincidunt velit quam, eu condimentum ligula bibendum ac. Duis volutpat mauris eu lacinia lobortis. Nulla facilisi. In accumsan sed massa sit amet pellentesque. Mauris tristique, nunc pharetra vestibulum tempus, ex sem molestie neque, ac varius risus lacus sit amet purus. Cras <span style="color:var(--green)">laoreet</span> dignissim tellus, ac congue augue. Donec blandit sem quis tortor hendrerit mattis. Mauris vitae ultricies libero. Curabitur suscipit dignissim augue, eleifend iaculis quam pellentesque eu. Sed pulvinar luctus sodales.</p>
    <div class="pill" style="left:75px;top:433px;width:46px;height:13px">GET STARTED</div>
    <div class="frame" style="left:310px;top:311px;width:40px;height:30px"></div>
    <div class="photo" style="left:344px;top:299px;width:152px;height:185px;background:linear-gradient(160deg,#c9c4bd,#8d8178 60%,#5c524c)" role="img" aria-label="Photo of a trainer with two clients holding a clipboard in a gym"></div>
    <div class="photo" style="left:292px;top:337px;width:58px;height:130px;background:linear-gradient(170deg,#d8d6d2,#7c7470)" role="img" aria-label="Photo of a trainer writing notes beside a client"></div>

    <!-- Why choose -->
    <div class="frame" style="left:95px;top:526px;width:40px;height:30px"></div>
    <div class="photo" style="left:128px;top:515px;width:152px;height:184px;background:linear-gradient(160deg,#e3e2e0,#b8b3ae 55%,#6f6a66)" role="img" aria-label="Photo of a coach guiding a woman through a side stretch"></div>
    <div class="photo" style="left:75px;top:552px;width:97px;height:130px;background:linear-gradient(170deg,#d2d0cc,#6e6965)" role="img" aria-label="Photo of a trainer and client reviewing a tablet"></div>
    <div class="abs label" style="left:325px;top:541px">Our Facilities, Uniqueness And Features</div>
    <div class="abs title" style="left:325px;top:557px">Why choose <em>Veltrafit</em></div>
    <p class="abs body" style="left:325px;top:576px;width:170px">Curabitur tincidunt velit quam, eu condimentum ligula bibendum ac. Duis volutpat mauris eu lacinia lobortis.</p>
    <ul class="abs checks" style="left:325px;top:598px">
      <li><svg viewBox="0 0 6 6"><path d="M.5 3.2 2.3 5 5.5 1" fill="none" stroke="#8a9a1b" stroke-width="1.2"/></svg>Lorem ipsum dolor sit amet</li>
      <li><svg viewBox="0 0 6 6"><path d="M.5 3.2 2.3 5 5.5 1" fill="none" stroke="#8a9a1b" stroke-width="1.2"/></svg>Consectetur adipiscing elit</li>
      <li><svg viewBox="0 0 6 6"><path d="M.5 3.2 2.3 5 5.5 1" fill="none" stroke="#8a9a1b" stroke-width="1.2"/></svg>Sed do eiusmod tempor incididunt</li>
      <li><svg viewBox="0 0 6 6"><path d="M.5 3.2 2.3 5 5.5 1" fill="none" stroke="#8a9a1b" stroke-width="1.2"/></svg>Ut labore et dolore magna aliqua.</li>
      <li><svg viewBox="0 0 6 6"><path d="M.5 3.2 2.3 5 5.5 1" fill="none" stroke="#8a9a1b" stroke-width="1.2"/></svg>Quis ipsum suspendisse ultrices gravida.</li>
    </ul>
    <div class="pill" style="left:325px;top:658px;width:46px;height:14px">GET STARTED</div>
    <div class="pill grey" style="left:378px;top:658px;width:44px;height:14px">BOOK NOW</div>

    <!-- Services -->
    <div class="abs label" style="left:75px;top:725px">Make A New Start With The New You</div>
    <div class="abs services-title" style="left:75px;top:742px">SERVICES FROM <em>VELTRAFIT</em></div>
    <p class="abs body" style="left:75px;top:763px;width:205px">Curabitur tincidunt velit quam, eu condimentum ligula bibendum ac. Duis volutpat mauris eu lacinia lobortis. Nulla facilisi. In accumsan sed massa sit amet pellentesque.</p>

    <article class="svc" style="left:75px;top:788px;background:linear-gradient(160deg,#7a1626,#a3303f 60%,#c7606a)" role="img" aria-label="Photo of a woman stretching in a red studio">
      <div class="veil"></div><h3>Studio Classes</h3><div class="rule"></div>
      <p>Curabitur tincidunt velit quam, eu condimentum ligula bibendum ac. Duis volutpat mauris eu lacinia lobortis. Nulla facilisi. In accumsan sed massa.</p>
      <div class="more">Know More <span>→</span></div>
    </article>
    <article class="svc" style="left:219px;top:788px;background:linear-gradient(160deg,#e3d3c5,#c4a896 60%,#9b8174)" role="img" aria-label="Photo of a live streamed yoga class recorded on a phone">
      <div class="veil"></div><h3>Live Classes</h3><div class="rule"></div>
      <p>Curabitur tincidunt velit quam, eu condimentum ligula bibendum ac. Duis volutpat mauris eu lacinia lobortis. Nulla facilisi. In accumsan sed massa.</p>
      <div class="more">Know More <span>→</span></div>
    </article>
    <article class="svc" style="left:362px;top:788px;background:linear-gradient(160deg,#a79a90,#6b5d55 55%,#3e3632)" role="img" aria-label="Photo of a man doing push-ups on medicine balls">
      <div class="veil"></div><h3>Personal Training</h3><div class="rule"></div>
      <p>Curabitur tincidunt velit quam, eu condimentum ligula bibendum ac. Duis volutpat mauris eu lacinia lobortis. Nulla facilisi. In accumsan sed massa.</p>
      <div class="more">Know More <span>→</span></div>
    </article>
    <article class="svc" style="left:75px;top:934px;background:linear-gradient(160deg,#8d8d86,#6f7a4a 55%,#9a8a3a)" role="img" aria-label="Photo of fresh vegetables, fruit and a measuring tape">
      <div class="veil"></div><h3>Diet Coaching</h3><div class="rule"></div>
      <p>Curabitur tincidunt velit quam, eu condimentum ligula bibendum ac. Duis volutpat mauris eu lacinia lobortis. Nulla facilisi. In accumsan sed massa.</p>
      <div class="more">Know More <span>→</span></div>
    </article>
    <article class="svc" style="left:219px;top:934px;background:linear-gradient(170deg,#8ea3b4,#5d6d79 55%,#7b6d5e)" role="img" aria-label="Photo of a woman doing squats on a seaside pier">
      <div class="veil"></div><h3>In-Person Workouts</h3><div class="rule"></div>
      <p>Curabitur tincidunt velit quam, eu condimentum ligula bibendum ac. Duis volutpat mauris eu lacinia lobortis. Nulla facilisi. In accumsan sed massa.</p>
      <div class="more">Know More <span>→</span></div>
    </article>
    <article class="svc" style="left:362px;top:934px;background:linear-gradient(160deg,#6c5a44,#8d7a63 55%,#4e5b3a)" role="img" aria-label="Photo of a man following a remote workout at home">
      <div class="veil"></div><h3>Remote Coaching</h3><div class="rule"></div>
      <p>Curabitur tincidunt velit quam, eu condimentum ligula bibendum ac. Duis volutpat mauris eu lacinia lobortis. Nulla facilisi. In accumsan sed massa.</p>
      <div class="more">Know More <span>→</span></div>
    </article>

    <!-- Featured -->
    <div class="abs title" style="left:75px;top:1096px">We <em>Featured</em> in</div>
    <div class="abs press">
      <span>LUMEN</span><span>The Daily Orbit</span><span>The Courier</span><span>MARLO</span><span>GLEAMWAY</span>
      <span>The Warden</span><span>Evening Ledger</span><span>BAZELLE</span><span>Fortane</span><span>WellForm</span>
    </div>

    <!-- Testimonials -->
    <div class="abs label" style="left:75px;top:1225px">Our Testimonials</div>
    <div class="abs t-heading" style="left:75px;top:1241px">Just don't listen to us,<br>check What People<br>think about us</div>
    <div class="abs stars" style="left:75px;top:1283px">★★★★★</div>
    <div class="abs rating" style="left:75px;top:1295px">Searchly Rating</div>
    <div class="abs stars" style="left:75px;top:1315px">★★★★★</div>
    <div class="abs rating" style="left:75px;top:1328px">ABCD Rating</div>
    <div class="pill" style="left:75px;top:1354px;width:75px;height:13px">CHECK ALL TESTIMONIALS</div>

    <div class="t-card" style="left:183px">
      <div class="avatar" style="background:linear-gradient(#f2f2f2,#d7d4d0)" role="img" aria-label="Portrait photo of the reviewer"></div>
      <div class="name">Milo Arden</div><div class="role">Marketing Manager, ABCD</div><div class="stars">★★★★★</div>
      <p>Lorem ipsum dolor sit amet, consectetur adipiscing elit, sed do eiusmod tempor incididunt ut labore et dolore magna aliqua. Quis ipsum suspendisse ultrices gravida. Risus commodo viverra maecenas accumsan lacus vel facilisis.</p>
    </div>
    <div class="t-card" style="left:328px">
      <div class="avatar" style="background:linear-gradient(#8f8f8f,#3f3a38)" role="img" aria-label="Portrait photo of the reviewer"></div>
      <div class="name">Selene Okafor</div><div class="role">Ex Model, Reporter</div><div class="stars">★★★★★</div>
      <p>Lorem ipsum dolor sit amet, consectetur adipiscing elit, sed do eiusmod tempor incididunt ut labore et dolore magna aliqua. Quis ipsum suspendisse ultrices gravida. Risus commodo viverra maecenas accumsan lacus vel facilisis.</p>
    </div>
    <div class="t-card" style="left:473px">
      <div class="avatar" style="background:linear-gradient(#e8c9b5,#9b5a3f)" role="img" aria-label="Portrait photo of the reviewer"></div>
      <div class="name">Rowan Pike</div><div class="role">Motivational Speaker</div><div class="stars">★★★★★</div>
      <p>Lorem ipsum dolor sit amet, consectetur adipiscing elit, sed do eiusmod tempor incididunt ut labore et dolore magna aliqua. Quis ipsum suspendisse ultrices gravida. Risus commodo viverra maecenas accumsan lacus vel facilisis.</p>
    </div>

    <!-- Subscribe -->
    <div class="frame" style="left:75px;top:1427px;width:40px;height:60px"></div>
    <div class="frame br" style="left:168px;top:1480px;width:112px;height:76px"></div>
    <div class="photo" style="left:80px;top:1434px;width:193px;height:115px;background:linear-gradient(160deg,#d9d9d7,#9c9894 55%,#4b4644)" role="img" aria-label="Photo of a coach kneeling beside a client and taking notes"></div>
    <div class="abs label" style="left:325px;top:1433px">Change Your Life With Us</div>
    <div class="abs sub-title" style="left:325px;top:1449px"><em>Get</em> Latest Updates <em>subscribe</em> now</div>
    <div class="abs email">Enter Your Email Address<span class="pill">Subscribe Now</span></div>
    <p class="abs body" style="left:325px;top:1503px;width:170px;color:#222">By entering email and subscribe you get the following notification and other details Lorem ipsum dolor sit amet, consectetur adipiscing elit, sed do eiusmod tempor incididunt ut labore et dolore magna aliqua.</p>

    <!-- Footer -->
    <footer class="abs footer">
      <div class="abs f-brand"><span class="brand-name">VELTRAFIT</span><span class="brand-dot"></span></div>
      <div class="abs social" style="left:75px;top:85px"><span style="background:#222"></span><span style="background:#222"></span><span style="background:#222"></span><span style="background:#222"></span><span style="background:#222"></span></div>
      <div class="abs f-small" style="left:75px;top:106px;font-size:4.3px">Copyright © 2023, <span style="color:var(--green)">Veltrafit</span> All rights reserved.</div>
      <div class="abs f-head" style="left:183px;top:48px">QUICK LINKS</div>
      <div class="abs f-small" style="left:183px;top:63px">ABOUT | SERVICES | THE JOURNAL | BLOG | SHOP | CONTACT</div>
      <div class="abs f-head" style="left:183px;top:79px">CONNECT WITH US</div>
      <div class="abs f-small" style="left:183px;top:94px">info@veltrafit.com | support@veltrafit.com</div>
      <div class="abs f-links" style="left:397px;top:41px">Search<br>Privacy Policy<br>Terms of Service<br>Members</div>
      <div class="abs cards" style="left:397px;top:93px"><span></span><span></span><span></span><span></span><span></span><span></span></div>
    </footer>
  </main>
</div>
</body>
</html>
```